Door Company Flyer for October Hardware Sale

We are a door company and need a new flyer for a sale on hardware going on starting today thru the end of October (Oct 1st-Oct 31st) Our logo colors are gray, orange, and white. We need the 3 pictures of hardware included. Our company is TALVO Commercial Door, our supplier is Quorvane and the hardware on sale is Marten brand. We will need this in pdf format to print flyers and also a digital version to post on our website and social media.

```html
<!DOCTYPE html>
<html lang="en">
<head>
<meta charset="utf-8">
<title>TALVO Commercial Door – October Hardware Sale</title>
<link href="https://fonts.googleapis.com/css2?family=Oswald:wght@500;600&family=Poppins:wght@300;700;800&display=swap" rel="stylesheet">
<style>
  :root {
    --orange: #f07127;
    --orange-light: #f58f57;
    --charcoal: #3c3c3c;
    --charcoal-soft: #555555;
    --white: #ffffff;
    --page: #f4f5f7;
    --ink: #222222;
  }
  * { margin: 0; padding: 0; box-sizing: border-box; }
  html, body {
    width: 1200px; height: 994px; overflow: hidden;
    background: var(--page);
    font-family: "Poppins", sans-serif;
  }
  .flyer {
    position: absolute; left: 260px; top: 27px;
    width: 680px; height: 940px;
    background: linear-gradient(160deg, var(--white) 0%, #f3f3f3 100%);
    overflow: hidden;
    box-shadow: 0 20px 50px rgba(0,0,0,0.18);
  }
  .flyer-shapes { position: absolute; inset: 0; }

  .headline {
    position: absolute; left: 110px; top: 200px; width: 520px;
    transform: rotate(-18deg); transform-origin: left top;
  }
  .headline .kicker {
    font-family: "Oswald", sans-serif; font-weight: 600;
    font-size: 46px; color: var(--charcoal); letter-spacing: 0.5px;
    margin-left: 90px; line-height: 1.1;
  }
  .headline .sale-strip {
    display: inline-block; background: var(--orange-light);
    color: var(--white); font-weight: 800; font-size: 27px;
    padding: 4px 18px; letter-spacing: 0.5px; margin-top: 6px;
  }
  .headline .until {
    font-weight: 300; font-size: 19px; color: var(--charcoal);
    letter-spacing: 1px; margin: 6px 0 4px 70px;
  }
  .headline .dates {
    display: inline-block; background: var(--charcoal-soft);
    color: var(--white); font-family: "Oswald", sans-serif; font-weight: 600;
    font-size: 64px; line-height: 1; padding: 10px 22px 14px;
    margin-left: 20px;
  }

  .product-grid {
    position: absolute; left: 356px; top: 566px; width: 260px; height: 290px;
    transform: rotate(-14deg); transform-origin: left top;
  }
  .product-tile {
    position: absolute;
    background: radial-gradient(circle at 50% 50%, #f4f4f4 0%, #c9c9c9 100%);
  }
  .product-tile .brand {
    position: absolute; top: 8px; right: 10px;
    font-weight: 800; font-size: 14px; color: var(--charcoal); letter-spacing: 1px;
  }
  .tile-lever { left: 132px; top: 0; width: 128px; height: 128px; }
  .tile-closer { left: 0; top: 22px; width: 124px; height: 132px; }
  .tile-exit { left: 0; top: 164px; width: 230px; height: 120px; }

  .features {
    position: absolute; left: 70px; top: 640px; list-style: none;
  }
  .features li {
    font-weight: 800; font-size: 17px; color: var(--ink);
    display: flex; align-items: center; gap: 12px; margin-bottom: 6px;
  }
  .features li::before {
    content: ""; width: 11px; height: 13px; background: var(--charcoal);
  }
  .features li:nth-child(odd)::before { background: var(--orange); }

  .partners {
    position: absolute; left: 60px; top: 810px;
    display: flex; align-items: center; gap: 40px;
  }
  .partner {
    display: flex; align-items: center; gap: 10px;
    font-weight: 800; color: var(--charcoal); letter-spacing: 2px;
  }
  .partner .mark { width: 22px; height: 22px; background: var(--orange); }
  .partner.supplier { font-size: 20px; }
  .partner.company { font-size: 20px; }
  .partner.company small { font-size: 12px; letter-spacing: 1px; margin-left: 4px; }
</style>
</head>
<body>
  <main class="flyer">
    <svg class="flyer-shapes" width="680" height="940" viewBox="0 0 680 940" aria-hidden="true">
      <polygon points="0,0 190,0 0,150" fill="var(--orange-light)"/>
      <polygon points="160,0 680,0 680,26 125,26" fill="var(--charcoal)"/>
      <polygon points="95,40 680,48 680,58 85,50" fill="var(--orange)"/>
      <polygon points="680,300 680,640 470,640" fill="var(--orange)"/>
      <polygon points="680,640 680,820 560,820 600,640" fill="var(--orange)"/>
      <polygon points="0,898 680,878 680,890 0,910" fill="var(--orange)"/>
      <polygon points="0,918 680,898 680,940 0,940" fill="var(--orange)"/>
      <polygon points="540,940 680,940 680,810" fill="var(--charcoal)"/>
      <polygon points="70,250 90,262 72,268" fill="var(--orange)"/>
      <polygon points="585,385 620,378 612,392" fill="var(--orange)"/>
      <polygon points="585,400 622,398 600,410" fill="var(--charcoal)"/>
      <polygon points="60,520 95,516 80,530" fill="var(--orange)"/>
      <polygon points="62,540 96,532 84,548" fill="var(--charcoal)"/>
    </svg>

    <section class="headline">
      <p class="kicker">STARTING TODAY!</p>
      <p class="sale-strip">HARDWARE SALE IS ONGOING</p>
      <p class="until">UNTIL THE END OF OCTOBER.</p>
      <p class="dates">OCT 1ST-OCT 31ST</p>
    </section>

    <section class="product-grid">
      <div class="product-tile tile-lever" role="img" aria-label="Photo of a Marten cylindrical lever lock"><span class="brand">MARTEN</span></div>
      <div class="product-tile tile-closer" role="img" aria-label="Photo of a Marten door closer"><span class="brand">MARTEN</span></div>
      <div class="product-tile tile-exit" role="img" aria-label="Photo of a Marten exit device push bar"><span class="brand">MARTEN</span></div>
    </section>

    <ul class="features">
      <li>DURABLE MATERIALS</li>
      <li>ERGONOMIC DESIGN</li>
      <li>HIGH SECURITY</li>
      <li>EASY INSTALLATION</li>
    </ul>

    <footer class="partners">
      <div class="partner supplier"><span class="mark"></span>QUORVANE</div>
      <div class="partner company">TALVO<small>COMMERCIAL DOOR</small></div>
    </footer>
  </main>
</body>
</html>
```